Kiswa Design

We need a flyer design for a product that we are a selling, a sacred Islamic cloth called a Kiswah, which is draped around the holy Kaaba in mecca every year.

The details we would like on the flyer are as follows:

Rare Kiswah of the holy Kaaba for sale (fitted in 1977 and 1982 vintage). For sale:

1) whole piece 15 meters x 2.60 meters : £60,000
2) 8 meters x 2.60 meters : £31,200
3) 4 meters x 2.60 meters : £15,600
4) 1 meter : £1500

(insert a high quality picture of holy Kaaba here, then underneath the picture, write the following:) "The Kaaba is covered by an expensive black cloth which is known as 'Kiswah' which is produced and changed every year"

(insert picture of our product here,i.e. use the document named MAIN IMAGE then underneath this picture write the following:) "Silk lampas weave Kiswah, woven silk on a black satin ground with Quranic calligraphy, the zig-zag bands of inscription alternate with the Shahadah and the inscription, 'God, exalted be His Glory!"

insert another picture of kiswah which i provided anywhere you like

(somewhere on flyer write the following) please note a percentage of sales will go towards Sadaqah for our Muslim brothers and sisters in need around the world

(somewhere on flyer write the following) Hallorand's international auction house authenticity document also available to prove the Kiswah is genuine.

100% genuine

contact us today! deals this good don't last forever.

email: relicoffer@tarnwickmail.com

Please use the images that I have attached on the flyer accordingly. Also feel free to be as creative as possible I want it to attract a lot of attention but also look professional so you may add some things to improve the look of the flyer.

note: the product being sold is on the pictures I've provided, in particular, i want file 2 "main image" in a large size on the flyer!

thank you! and happy holidays

Muslims and Islamic collectors

House

• the dimensions of the flyer is :
• A5 horizontal or vertical
• (210 x 148 mm)
• must have colors! up to you what colors to choose!

```html
<!DOCTYPE html>
<html lang="en">
<head>
<meta charset="utf-8">
<title>Rare Kiswa of the Holy Kaa'ba – For Sale</title>
<link rel="stylesheet" href="https://fonts.googleapis.com/css2?family=Open+Sans:ital,wght@0,400;0,600;0,700;0,800;1,700;1,800&family=Anton&display=swap">
<style>
  :root {
    --green: #1f6043;
    --sand: #ddcd96;
    --sand-text: #e5d59e;
    --brown: #a0592d;
    --brown-text: #9b5a2c;
    --black: #000000;
    --white: #ffffff;
    --grey-light: #e2e2e2;
    --grey-mid: #c4c4c4;
  }
  * { margin: 0; padding: 0; box-sizing: border-box; }
  html, body { width: 846px; height: 1200px; overflow: hidden; background: #fff; }
  .flyer {
    position: relative;
    width: 846px;
    height: 1200px;
    font-family: "Open Sans", Arial, sans-serif;
    overflow: hidden;
  }
  .band { position: absolute; left: 0; width: 846px; }

  .for-sale {
    top: 0; height: 108px;
    background: var(--green);
    color: var(--sand-text);
    font-weight: 700;
    font-size: 108px;
    letter-spacing: 11px;
    line-height: 104px;
    text-align: center;
  }
  .title {
    top: 108px; height: 190px;
    background: var(--sand);
    color: var(--green);
    text-align: center;
  }
  .title h1 {
    font-weight: 800;
    font-size: 62px;
    line-height: 70px;
    padding-top: 4px;
    letter-spacing: 1.5px;
  }
  .title .vintage {
    color: var(--black);
    font-weight: 700;
    font-style: italic;
    font-size: 26px;
    line-height: 34px;
    margin-top: 0;
  }
  .genuine {
    top: 298px; height: 78px;
    background: var(--brown);
    color: var(--white);
    font-weight: 700;
    font-size: 76px;
    line-height: 80px;
    text-align: center;
  }

  .gallery {
    top: 376px; height: 394px;
    background: linear-gradient(135deg, var(--grey-light), var(--grey-mid) 50%, var(--grey-light));
  }
  .photo-kaaba {
    position: absolute; left: 0; top: 2px; width: 380px; height: 228px;
    background: linear-gradient(180deg, #c9c6bd 0%, #8f8877 22%, #232323 40%, #1c1c1c 62%, #6a5b42 80%, #8b8170 100%);
  }
  .caption {
    position: absolute; left: 10px; top: 234px; width: 345px;
    font-weight: 700; font-size: 15.5px; line-height: 19px; color: var(--black);
    letter-spacing: -0.3px;
  }
  .photo-cloth {
    position: absolute; left: 552px; top: 2px; width: 294px; height: 392px;
    background: linear-gradient(160deg, #ececec 0%, #4a4a4a 20%, #1e1e1e 55%, #3c3c3c 85%, #e0e0e0 100%);
  }

  .price-panel {
    top: 770px; height: 292px;
    background: var(--black);
    color: var(--white);
  }
  .price-list {
    list-style: none;
    position: absolute; left: 78px; top: 12px;
    font-weight: 700; font-size: 25.5px; line-height: 40px;
  }
  .authenticity {
    position: absolute; left: 0; top: 178px; width: 846px;
    text-align: center; font-size: 21px; line-height: 28px;
  }
  .sadaqah {
    position: absolute; left: 0; top: 260px; width: 846px;
    text-align: center; font-weight: 700; font-style: italic; font-size: 14.5px;
    letter-spacing: -0.2px;
  }

  .call-to-action {
    top: 1062px; height: 46px;
    background: var(--sand);
    color: var(--brown-text);
    font-family: "Anton", Impact, sans-serif;
    font-size: 30px;
    line-height: 46px;
    text-align: center;
    letter-spacing: 0.3px;
  }
  .contact {
    top: 1108px; height: 92px;
    background: var(--green);
    color: var(--sand-text);
    font-size: 58px;
    line-height: 88px;
    text-align: center;
  }
</style>
</head>
<body>
<main class="flyer">
  <div class="band for-sale">FOR SALE</div>

  <header class="band title">
    <h1>Rare Kiswa<br>of the Holy Kaa’ba</h1>
    <p class="vintage">Fitted in 1977 and 1982 Vintage</p>
  </header>

  <div class="band genuine">100% GENUINE</div>

  <section class="band gallery" role="img" aria-label="Faint grey Quranic calligraphy pattern background">
    <div class="photo-kaaba" role="img" aria-label="Photograph of the Kaaba draped in its black kiswa surrounded by pilgrims"></div>
    <p class="caption">The Kaa’ba is covered by a black cloth known as ‘kiswa’ which is produced and changed every year.</p>
    <div class="photo-cloth" role="img" aria-label="Photograph of the folded black silk kiswa cloth for sale"></div>
  </section>

  <section class="band price-panel">
    <ol class="price-list">
      <li>1) whole piece, 15 meters x 2.60 meters : £60,000</li>
      <li>2) 8 meters x 2.60 meters : £31,200</li>
      <li>3) 4 meters x 2.60 meters : £15,600</li>
      <li>4) 1 meter : £1500</li>
    </ol>
    <p class="authenticity">Hallorand's international auction house authenticity document<br>also availableto prove the Kiswa is genuine.</p>
    <p class="sadaqah">A percentage of sales will go towards Sadaqah for ourMuslim brothers and sisters in need around the world</p>
  </section>

  <div class="band call-to-action">Contact us today! Deals this good don't last forever.</div>

  <footer class="band contact">relicoffer@tarnwickmail.com</footer>
</main>
</body>
</html>
```